BHSC Business cards

We are an established dental practice that is looking for new business cards to match our new logo. We are looking for something unique and sophisticated.
BRIEF: Colours are black, silver and white. Include the company name, logo (including “Pelwick Heath Dental Care”) and phone number “03 9415 2876”.
Front - Include the company name, logo (including “Pelwick Heath Dental Care”) and phone number “03 9415 2876”.
Back - Include the company name,  “Pelwick Heath Dental Care”, phone number “03 9415 2876”. address "64A Tindle Street, Pelwick Heath, Vic 3187", "Email reception@pelwickheathdentalcare.com.au", the Dentist Name " Dr ................................"  Your next appointment "Day, date and time(am/pm)".  3 lines for 3 appointments please, and at the bottom "IF UNABLE TO KEEP THIS APPOINTMENT 48 HOURS NOTICE IS REQUIRED."
Try and be creative and different with the design, i've added an image for inspiration

Target Market(s)
ALL in need of dental
Industry/Entity Type
Dental Clinic
Look and feel
Each slider illustrates characteristics of the customer's brand and the style your logo design should communicate.

```html
<!DOCTYPE html>
<html lang="en">
<head>
<meta charset="utf-8">
<title>Pelwick Heath Dental Care – Business Cards</title>
<link href="https://fonts.googleapis.com/css2?family=Montserrat:wght@700&family=Roboto:wght@400;700&display=swap" rel="stylesheet">
<style>
  :root {
    --backdrop: #cdb99c;
    --card-dark: #2b2b2b;
    --card-light: #ffffff;
    --ink: #1c1c1c;
    --ink-soft: #3a3a3a;
    --paper-white: #ffffff;
    --silver-faint: #ececec;
  }
  * { margin: 0; padding: 0; box-sizing: border-box; }
  html, body { width: 1200px; height: 900px; overflow: hidden; }
  body { background: var(--backdrop); position: relative; font-family: "Roboto", Arial, sans-serif; color: var(--ink); }

  .card { position: absolute; left: 312px; width: 576px; height: 329px; overflow: hidden; }
  .card--front { top: 98px; background: var(--card-dark); }
  .card--back { top: 472px; background: var(--card-light); }

  .brand { font-family: "Montserrat", Arial, sans-serif; font-weight: 700; text-transform: uppercase; }
  .brand__line { display: block; white-space: nowrap; }

  /* Front */
  .front-lockup { position: absolute; left: 92px; top: 131px; display: flex; align-items: center; gap: 14px; color: var(--paper-white); }
  .front-lockup .mark { width: 66px; height: 66px; border: 3px solid var(--paper-white); border-radius: 50%; flex: none; }
  .front-lockup .brand__line--name { font-size: 30px; line-height: 32px; letter-spacing: 0.2px; }
  .front-lockup .brand__line--sub { font-size: 15px; line-height: 18px; letter-spacing: 2.4px; }

  /* Back */
  .back-watermark { position: absolute; left: 253px; top: 12px; width: 300px; height: 300px; border: 14px solid var(--silver-faint); border-radius: 50%; }
  .back-header { position: absolute; left: 24px; top: 28px; display: flex; align-items: center; }
  .back-header .brand { color: var(--ink); padding-right: 10px; border-right: 1.5px solid var(--ink); }
  .back-header .brand__line--name { font-size: 20px; line-height: 22px; }
  .back-header .brand__line--sub { font-size: 10.5px; line-height: 14px; letter-spacing: 1.5px; }
  .contact { padding-left: 10px; font-size: 14.5px; line-height: 20px; color: var(--ink-soft); }

  .fill-row { position: absolute; display: flex; align-items: baseline; font-size: 14.5px; color: var(--ink-soft); }
  .fill-row .dots { flex: 1; border-bottom: 1.5px dotted #555; margin: 0 2px; transform: translateY(-3px); }
  .dentist { left: 23px; top: 88px; width: 526px; font-weight: 700; font-size: 15px; }

  .appointments-title { position: absolute; left: 181px; top: 130px; width: 214px; text-align: center; font-size: 16.5px; padding-bottom: 6px; border-bottom: 1.5px solid var(--ink); color: var(--ink); }

  .appt { left: 23px; width: 530px; }
  .appt .dots--date { flex: none; width: 202px; }
  .appt--1 { top: 178px; }
  .appt--2 { top: 211px; }
  .appt--3 { top: 243px; }

  .notice { position: absolute; left: 0; right: 0; top: 293px; text-align: center; font-size: 12.5px; color: var(--ink); }
  .notice strong { font-weight: 700; }
</style>
</head>
<body>

  <section class="card card--front" aria-label="Business card front">
    <div class="front-lockup">
      <span class="mark" aria-hidden="true"></span>
      <div class="brand">
        <span class="brand__line brand__line--name">Pelwick Heath</span>
        <span class="brand__line brand__line--sub">Dental Care — 03 9415 2876</span>
      </div>
    </div>
  </section>

  <section class="card card--back" aria-label="Appointment card back">
    <span class="back-watermark" aria-hidden="true"></span>

    <header class="back-header">
      <div class="brand">
        <span class="brand__line brand__line--name">Pelwick Heath</span>
        <span class="brand__line brand__line--sub">Dental Care — 03 9415 2876</span>
      </div>
      <address class="contact" style="font-style:normal">
        64A Tindle Street, Pelwick Heath, Vic 3187<br>
        reception@pelwickheathdentalcare.com.au
      </address>
    </header>

    <div class="fill-row dentist"><span>Dr</span><span class="dots"></span></div>

    <h2 class="appointments-title" style="font-weight:400">YOUR NEXT APPOINTMENT</h2>

    <div class="fill-row appt appt--1"><span>Date</span><span class="dots dots--date"></span><span>Time</span><span class="dots"></span><span>am/pm</span></div>
    <div class="fill-row appt appt--2"><span>Date</span><span class="dots dots--date"></span><span>Time</span><span class="dots"></span><span>am/pm</span></div>
    <div class="fill-row appt appt--3"><span>Date</span><span class="dots dots--date"></span><span>Time</span><span class="dots"></span><span>am/pm</span></div>

    <p class="notice">IF UNABLE TO KEEP THIS APPOINTMENT <strong>48</strong> HOURS NOTICE IS REQUIRED.</p>
  </section>

</body>
</html>
```